Simple elegant business card

General card for a fin and television director.
Just want name, email, phone and address.

Target Market(s)

Prospective employers

Industry/Entity Type

Business

Requirements
Must have
• As above
Nice to have
• Logo but not necessary.
Should not have
• Not too colourful or funky.
• Simplicity and elegance the way to go.

```html
<!DOCTYPE html>
<html lang="en">
<head>
<meta charset="utf-8">
<title>Nora Ellis — Business Card</title>
<link rel="stylesheet" href="https://fonts.googleapis.com/css2?family=Source+Sans+3:wght@400;600&display=swap">
<style>
  :root {
    --backdrop: #e8e6e2;
    --card: #ffffff;
    --ink: #8c8c8c;
    --ink-soft: #9a9a9a;
    --rule: #a6a6a6;
    --shadow: rgba(60, 50, 35, 0.18);
  }
  html, body {
    margin: 0;
    padding: 0;
    width: 1200px;
    height: 1000px;
    overflow: hidden;
    background: var(--backdrop);
    font-family: "Source Sans 3", "Myriad Pro", Arial, sans-serif;
  }
  .canvas {
    position: relative;
    width: 1200px;
    height: 1000px;
  }
  .card {
    position: absolute;
    left: 220px;
    width: 760px;
    height: 434px;
    background: var(--card);
    box-shadow: 0 2px 3px var(--shadow), 0 14px 30px var(--shadow);
  }
  .card--front { top: 52px; }
  .card--back { top: 514px; }

  .identity {
    position: absolute;
    top: 48px;
    right: 48px;
    margin: 0;
    font-size: 34px;
    font-weight: 600;
    letter-spacing: 0.5px;
    line-height: 1.2;
    color: var(--ink);
  }

  .contact {
    position: absolute;
    top: 40px;
    right: 44px;
    border: 1.5px solid var(--rule);
    padding: 10px 22px 12px 20px;
    color: var(--ink-soft);
    font-size: 21px;
    font-style: normal;
    font-weight: 400;
    line-height: 1.22;
  }
  .contact__line {
    display: block;
    margin: 0;
  }
</style>
</head>
<body>
  <main class="canvas">
    <section class="card card--front" aria-label="Card front">
      <h1 class="identity">Nora Ellis</h1>
    </section>

    <section class="card card--back" aria-label="Card back">
      <address class="contact">
        <span class="contact__line">218 Harbor st</span>
        <span class="contact__line">Bayview CA USA</span>
        <span class="contact__line">noraellis@mail.com</span>
        <span class="contact__line">+1 555 014 2287</span>
      </address>
    </section>
  </main>
</body>
</html>
```